Natural Skincare Company Needs Label Design

We need a label design for the first product of a new company called 'Vela'. We make skincare products made from natural ingredients.
Our initial product is a rose hip oil, and we need a label for the small 30mL bottle that it comes in, as well as for the box that the bottle will be sold in. The label will be printed directly onto the bottle, like the example in the attached photo. For reference, we like the look and feel of the labels on the bottle and box in the attached photos. It should convey a sense of natural.
The bottle will be dark green glass. For the name 'Vela' we like something close to orange so that it stands out. The rest of the text on the front of the bottle and box should read 'natural skincare' 'pure & organic' 'Rose hip oil' 'huile de cynorrhodon' 'pure et biologique'. '30mL' '1fl.oz'
We also like the silhouette of the main ingredient like in the attached photo. So a silhouette of a rose hip on the front of the bottle and box would be preferred.
On the right side of the bottle and box:
'Rose hip oil'
'Ingredients: 100% natural, cold pressed, Rosa canina (rose hip) seed oil'
'Benefits: Hydrates and refreshes skin, leaving a more even skin tone and a healthy glow'
'Application: Massage 3-4 drops into clean, damp skin twice daily or as required'
'Suitable for all skin types'
'Store below 30C'
On the left side of the bottle and box:
'Huile de Cynorrhodon'
'Ingredients/Constituants: huile de Rosa canina (cynorrhodon) 100% naturel, presse a froid'
'Bienfaits: rafraichit la peau, teint eblouissant'
'Mode d'emploi: Massez 3 a 4 gouttes sur une peau propre et humide deluxe fois par jour'
'Convient a tous les types de peau'
'Conserver a moins de 30C'

```html
<!DOCTYPE html>
<html lang="en">
<head>
<meta charset="UTF-8">
<title>Vela Rose Hip Oil – Bottle Label</title>
<link rel="stylesheet" href="https://fonts.googleapis.com/css2?family=Cinzel:wght@400;600&family=Cormorant+Garamond:wght@500&display=swap">
<style>
  :root {
    --page-bg: #ffffff;
    --glass-light: #2a7a3a;
    --glass-dark: #0f3a1a;
    --cap-black: #111111;
    --cap-edge: #2b2b2b;
    --brand-orange: #e8901c;
    --label-white: #f2f5ef;
    --leaf-sage: #9cc4a6;
  }
  html, body {
    margin: 0;
    padding: 0;
    width: 1200px;
    height: 1000px;
    overflow: hidden;
    background: var(--page-bg);
  }
  .canvas { display: block; width: 1200px; height: 1000px; }
  .cap { fill: var(--cap-black); }
  .cap-ring { fill: none; stroke: var(--cap-edge); stroke-width: 2; }
  .glass { fill: url(#glassGradient); }
  .illustration { fill: var(--leaf-sage); opacity: .85; }
  .brand-name {
    font-family: "Cinzel", serif;
    font-weight: 400;
    font-size: 64px;
    fill: var(--brand-orange);
  }
  .product-name {
    font-family: "Cinzel", serif;
    font-weight: 600;
    font-size: 27px;
    fill: var(--brand-orange);
  }
  .product-name-fr {
    font-family: "Cinzel", serif;
    font-size: 12.5px;
    letter-spacing: .8px;
    fill: var(--label-white);
  }
  .claim-orange {
    font-family: "Cinzel", serif;
    font-size: 12.5px;
    letter-spacing: 1.6px;
    fill: var(--brand-orange);
  }
  .claim-white {
    font-family: "Cormorant Garamond", serif;
    font-weight: 500;
    font-size: 12.5px;
    letter-spacing: .8px;
    fill: var(--label-white);
  }
  .volume {
    font-family: "Cinzel", serif;
    font-size: 13px;
    letter-spacing: .6px;
    fill: var(--brand-orange);
  }
  .storage {
    font-family: "Cormorant Garamond", serif;
    font-weight: 500;
    font-size: 12px;
    letter-spacing: .8px;
    fill: var(--label-white);
  }
  .rule { stroke: var(--label-white); stroke-width: 1.2; }
  .icon-line { fill: none; stroke: var(--label-white); stroke-width: 2.2; stroke-linejoin: round; stroke-linecap: round; }
  .icon-text { font-family: "Cinzel", serif; font-size: 8px; fill: var(--label-white); }
</style>
</head>
<body>
<svg class="canvas" viewBox="0 0 1200 1000" xmlns="http://www.w3.org/2000/svg">
  <defs>
    <linearGradient id="glassGradient" x1="0" y1="0" x2="1" y2="0">
      <stop offset="0" stop-color="var(--glass-dark)"/>
      <stop offset=".45" stop-color="var(--glass-light)"/>
      <stop offset="1" stop-color="var(--glass-dark)"/>
    </linearGradient>
    <g id="bottleShape">
      <path class="glass" d="M258 490 Q258 452 300 446 L490 446 Q532 452 532 490 L532 944 Q532 956 520 956 L270 956 Q258 956 258 944 Z"/>
      <path class="cap" d="M330 240 L330 84 Q330 20 394 20 Q458 20 458 84 L458 240 Z"/>
      <rect class="cap" x="282" y="220" width="226" height="160" rx="20"/>
      <rect class="cap" x="270" y="370" width="250" height="86" rx="8"/>
      <line class="cap-ring" x1="274" y1="404" x2="516" y2="404"/>
      <line class="cap-ring" x1="274" y1="414" x2="516" y2="414"/>
    </g>
  </defs>

  <!-- Front of bottle -->
  <g class="bottle bottle-front">
    <use href="#bottleShape"/>
    <rect class="illustration" x="352" y="535" width="144" height="125" rx="36"
          role="img" aria-label="Silhouette of a rose hip sprig with berries and leaves"/>
    <text class="brand-name" x="395" y="728" text-anchor="middle">Vela</text>
    <text class="product-name" x="395" y="774" text-anchor="middle">ROSE HIP OIL</text>
    <text class="product-name-fr" x="395" y="798" text-anchor="middle">HUILE DE CYNORRHODON</text>
    <text class="claim-orange" x="395" y="845" text-anchor="middle">NATURAL SKINCARE</text>
    <text class="claim-white" x="395" y="865" text-anchor="middle">PURE &amp; ORGANIC</text>
    <line class="rule" x1="298" y1="874" x2="492" y2="874"/>
    <text class="claim-white" x="395" y="890" text-anchor="middle">PURE ET BIOLOGIQUE</text>
    <text class="volume" x="395" y="914" text-anchor="middle">30ML 1FL.OZ</text>
  </g>

  <!-- Back of bottle -->
  <g class="bottle bottle-back" transform="translate(420 0)">
    <use href="#bottleShape"/>
    <rect class="illustration" x="274" y="555" width="246" height="255" rx="60"
          role="img" aria-label="Scattered rose hip leaf sprig silhouettes"/>
    <text class="storage" x="397" y="846" text-anchor="middle">STORE BELOW 30C</text>
    <line class="rule" x1="300" y1="854" x2="494" y2="854"/>
    <text class="storage" x="397" y="870" text-anchor="middle">CONSERVER A MOINS DE 30C</text>
    <g class="icon-recycle" transform="translate(371 906)">
      <path class="icon-line" d="M-4 -10 L4 -10 L9 -2 M9 -2 L11 -7 M9 -2 L4 -3"/>
      <path class="icon-line" d="M11 4 L7 11 L-3 11 M-3 11 L0 8 M-3 11 L0 14"/>
      <path class="icon-line" d="M-9 6 L-12 0 L-8 -7 M-8 -7 L-9 -2 M-8 -7 L-3 -6"/>
    </g>
    <g class="icon-pao" transform="translate(423 906)">
      <path class="icon-line" d="M-12 -4 L12 -4 L10 12 L-10 12 Z"/>
      <path class="icon-line" d="M-12 -8 L8 -15"/>
      <text class="icon-text" x="0" y="8" text-anchor="middle">6M</text>
    </g>
  </g>
</svg>
</body>
</html>
```